依頼詳細
ポスティング用のチラシです。
思わず手に取って見たくなるようなデザインとキャッチャーなコピーを
ご提案ください。

原稿にイラストを入れましたが、写真でも構いません。
また、全体のレイアウトも自由に変更頂いて構いません。

尚、コンペで表面が決まりましたら、裏面に着手していただきますので、
ご承知おきください。

それではご提案お待ちしております。
何卒よろしくお願い申し上げます。

記載項目
原稿にまとめました
サイズ
A4
ページ数
両面
希望イメージ
シンプル 複雑
単色 カラフル
暗い 明るい
日常 高級
遊び心 厳粛
未来的 伝統的
女性的 男性的
希望する色
納品ファイル
• イラストレーター形式 (.ai)
補足説明
お世話様でございます。
どれも素晴らしいご提案、誠にありがとうございました。
検討させていただきますので、決定までにしばらくお時間くださいませ。
宜しくお願い申し上げます。
■ 選んだ理由

インパクトのあるアイキャッチ(イラスト・コピー)と、非常に分かり易くまとめて頂いた所が
ポイントです。

■ 提案者全員のお礼・コメント

この度は素晴らしい作品をご提案頂きまして、誠にありがとうございました。
また機会を作りますので、今後ともよろしくお願い申し上げます。

```html
<!DOCTYPE html>
<html lang="ja">
<head>
<meta charset="utf-8">
<title>メガネ出張サービス</title>
<link href="https://fonts.googleapis.com/css2?family=M+PLUS+Rounded+1c:wght@500;700;800;900&family=Noto+Sans+JP:wght@400;500;700;900&display=swap" rel="stylesheet">
<style>
:root{
  --navy:#1d3a6e;
  --blue:#2f8fd6;
  --sky:#d9eefb;
  --pale:#eef7fd;
  --red:#e3312d;
  --yellow:#ffe14d;
  --orange:#f39a1e;
  --ink:#333;
  --white:#fff;
}
*{box-sizing:border-box;margin:0;padding:0}
html,body{width:849px;height:1200px;overflow:hidden}
body{font-family:"Noto Sans JP",sans-serif;color:var(--ink);background:var(--white)}
.flyer{position:relative;width:849px;height:1200px;overflow:hidden;background:linear-gradient(var(--white) 0,var(--white) 540px,var(--pale) 540px)}
.headline{position:absolute;top:16px;left:0;width:100%;text-align:center;font-family:"M PLUS Rounded 1c",sans-serif;font-weight:900;color:var(--navy);font-size:46px;line-height:1.15;white-space:nowrap}
.headline b{font-size:34px}
.hero-art{position:absolute;top:132px;left:305px;width:240px;height:188px;border-radius:50% 50% 14px 14px;background:radial-gradient(circle at 50% 40%,#f7e3d4,#e8d3f0 60%,#cfe3f5)}
.bubble{position:absolute;background:var(--white);border:2px solid var(--navy);border-radius:50%;font-weight:700;font-size:14px;line-height:1.35;text-align:center;display:flex;align-items:center;justify-content:center;color:var(--navy)}
.bubble.b1{top:140px;left:150px;width:140px;height:90px}
.bubble.b2{top:232px;left:82px;width:118px;height:76px}
.bubble.b3{top:140px;left:568px;width:118px;height:80px}
.bubble.b4{top:222px;left:640px;width:150px;height:94px;font-size:13px}
.sparkle{position:absolute;width:40px;height:40px;border-radius:50%;background:var(--yellow)}
.title{position:absolute;top:326px;left:0;width:100%;text-align:center;font-family:"M PLUS Rounded 1c",sans-serif;font-weight:900}
.title .pill{display:inline-block;background:var(--red);color:var(--white);font-size:60px;line-height:1;padding:14px 50px;border-radius:60px;letter-spacing:4px}
.title .big{display:block;margin-top:4px;font-size:96px;line-height:1.05;color:var(--navy);letter-spacing:6px}
.visit{position:absolute;top:330px;left:612px;width:170px;height:84px;background:var(--blue);color:var(--white);border-radius:46px;font-family:"M PLUS Rounded 1c",sans-serif;font-weight:800;font-size:20px;line-height:1.25;text-align:center;display:flex;align-items:center;justify-content:center}
.band{position:absolute;top:560px;left:28px;width:793px;height:36px;background:var(--blue);color:var(--white);font-weight:700;font-size:16px;text-align:center;line-height:36px;border-radius:4px}
.steps{position:absolute;top:606px;left:28px;width:793px;display:grid;grid-template-columns:repeat(4,1fr);gap:10px}
.step .cap{display:flex;align-items:center;gap:6px;font-size:13px;font-weight:700;color:var(--navy);margin-bottom:6px;line-height:1.25;min-height:34px}
.step .num{flex:none;width:22px;height:22px;border-radius:4px;background:var(--navy);color:var(--white);font-size:13px;text-align:center;line-height:22px}
.step .photo{height:100px;border-radius:4px;background:linear-gradient(135deg,#c8d2dc,#8fa2b5)}
.step .note{font-size:9px;color:#666;margin-top:3px}
.lower{position:absolute;top:768px;left:28px;width:793px;height:322px}
.relief{position:absolute;left:0;top:0;width:400px;height:322px;background:var(--white);border-radius:10px;border:2px solid var(--sky)}
.woman{position:absolute;left:12px;top:20px;width:120px;height:260px;border-radius:60px 60px 10px 10px;background:linear-gradient(#f6d8c6,#9ec7e8)}
.relief h3{position:absolute;left:140px;top:20px;font-family:"M PLUS Rounded 1c",sans-serif;font-weight:900;color:var(--navy);font-size:26px;white-space:nowrap}
.relief h3 span{display:inline-block;background:var(--orange);color:var(--white);font-size:18px;border-radius:50%;width:46px;height:46px;line-height:46px;text-align:center;margin-right:8px}
.free{position:absolute;left:140px;top:84px;display:flex;gap:8px}
.free div{width:76px;height:76px;border-radius:50%;background:var(--orange);color:var(--white);font-weight:900;font-size:17px;line-height:1.2;display:flex;align-items:center;justify-content:center;text-align:center}
.safety{position:absolute;left:140px;top:180px;width:248px}
.safety .tag{background:var(--red);color:var(--white);font-weight:900;font-size:15px;text-align:center;border-radius:4px;padding:4px 0}
.safety .icons{display:flex;gap:8px;margin-top:10px}
.safety .icons i{flex:1;height:52px;border-radius:6px;background:var(--sky)}
.voices{position:absolute;left:412px;top:0;width:381px;height:322px}
.voices .head{display:inline-block;background:var(--orange);color:var(--white);font-weight:700;font-size:14px;padding:4px 16px;border-radius:14px}
.voice{margin-top:8px;background:var(--white);border-radius:8px;padding:10px 12px;font-size:12px;line-height:1.6;overflow:hidden}
.voice b{display:block;color:var(--navy);font-size:13px;margin-bottom:3px}
.voice .who{display:inline-block;width:60px;height:60px;float:right;margin-left:8px;border-radius:50%;background:#f7d9c4}
.consult{position:absolute;top:1100px;left:0;width:100%;text-align:center;font-weight:700;color:var(--navy);font-size:17px}
.footer{position:absolute;top:1132px;left:0;width:100%;height:68px;background:var(--yellow);display:flex;align-items:center;padding:0 30px}
.dog{width:110px;height:52px;border-radius:26px;background:linear-gradient(90deg,#c07a3a,#e0a060)}
.company{margin-left:30px;font-weight:700;color:var(--navy);font-size:16px;line-height:1.3}
.company small{display:block;font-size:11px;font-weight:500}
.tel{margin-left:auto;display:flex;align-items:center;gap:8px;font-family:"M PLUS Rounded 1c",sans-serif;font-weight:900;font-size:40px;color:var(--navy)}
</style>
</head>
<body>
<div class="flyer">
  <div class="headline">外出を<br>控えている方<b>のための</b></div>

  <span class="sparkle" style="top:60px;left:40px"></span>
  <span class="sparkle" style="top:40px;left:760px"></span>
  <div class="hero-art" role="img" aria-label="困った表情の高齢のご夫婦のイラスト"></div>
  <div class="bubble b1">新型<br>コロナウイルスで<br>外出が不安</div>
  <div class="bubble b2">家で<br>忘れがちで</div>
  <div class="bubble b3">おかけるのが<br>億劫</div>
  <div class="bubble b4">免許を<br>返納してしまって<br>お店にいけない</div>

  <div class="title"><span class="pill">メガネ</span><span class="big">出張サービス</span></div>
  <div class="visit">ご自宅まで<br>うかがいます</div>

  <div class="band">わざわざお店に行かなくて大丈夫。専用車でご自宅にうかがって、メガネをお作りいたします</div>

  <div class="steps">
    <div class="step"><div class="cap"><span class="num">1</span>視力測定車で<br>ご自宅にうかがいます</div><div class="photo" role="img" aria-label="視力測定車の写真"></div></div>
    <div class="step"><div class="cap"><span class="num">2</span>車内で視力検査</div><div class="photo" role="img" aria-label="車内の視力検査の写真"></div></div>
    <div class="step"><div class="cap"><span class="num">3</span>レンズ・フレームを<br>お選びいただきます</div><div class="photo" role="img" aria-label="並んだメガネフレームの写真"></div><div class="note">レンズ・フレームは各種ご用意しております</div></div>
    <div class="step"><div class="cap"><span class="num">4</span>ご注文後、自宅で<br>お受け取り</div><div class="photo" role="img" aria-label="メガネの受け渡しの写真"></div><div class="note">完成後にご自宅へお届けいたします</div></div>
  </div>

  <div class="lower">
    <div class="relief">
      <div class="woman" role="img" aria-label="案内する女性スタッフのイラスト"></div>
      <h3><span>安心</span>3つの無料</h3>
      <div class="free"><div>視力<br>測定</div><div>超音波<br>洗浄</div><div>ネジ<br>調整</div></div>
      <div class="safety"><div class="tag">感染対策強化中!!</div><div class="icons"><i role="img" aria-label="マスク着用のアイコン"></i><i role="img" aria-label="手指消毒のアイコン"></i><i role="img" aria-label="換気のアイコン"></i></div></div>
    </div>
    <div class="voices">
      <span class="head">お客様の声</span>
      <div class="voice"><span class="who" role="img" aria-label="お客様のイラスト"></span><b>[みどり市 A様 60代 女性]</b>外出を控えていたので、自宅まで来てくれて大変助かりました。丁寧に測ってもらえて安心でした。</div>
      <div class="voice"><span class="who" role="img" aria-label="お客様のイラスト"></span><b>[みどり市中町 C様 70代 男性]</b>免許を返納してお店に行けずに困っていました。家でゆっくり選べて、とても満足しています。</div>
    </div>
  </div>

  <div class="consult">メガネのことなら何でもご相談ください</div>
  <div class="footer">
    <div class="dog" role="img" aria-label="ダックスフンドのキャラクター"></div>
    <div class="company">株式会社ミライ めがねのミライ<small>青空県みどり市 1-2-3</small></div>
    <div class="tel">
      <svg width="40" height="40" viewBox="0 0 24 24" aria-hidden="true"><path fill="#1d3a6e" d="M6.6 10.8a15.1 15.1 0 0 0 6.6 6.6l2.2-2.2a1 1 0 0 1 1-.25 11.4 11.4 0 0 0 3.6.57 1 1 0 0 1 1 1V20a1 1 0 0 1-1 1A17 17 0 0 1 3 4a1 1 0 0 1 1-1h3.5a1 1 0 0 1 1 1c0 1.25.2 2.45.57 3.57a1 1 0 0 1-.25 1z"/></svg>
      0120-00-4321
    </div>
  </div>
</div>
</body>
</html>
```